Business Card Design

Motorvane Ledger is an online automotive resource on a national scale specifically targeting lease purchases for new cars. Our Online and app platform allow prospective lease clients to scan a window sticker while at a franchise dealership and instantly receive a lease quote at what we call the sweet spot. Motorvane Ledger offers price transparency during the lease process to allow average people the confidence in the lease process and takes away any fear of the big franchise dealers.
Motorvane ledger allows ordinary lease customers to know they are getting a low price lease and not overpaying. Never overpay again

Industry/Entity Type

Automotive

Contact Information for Business Card

Motorvane Ledger
Martin Sowerby (President of operations)
Phone: 888-247-6031
Cell: 561-384-2706

```html
<!DOCTYPE html>
<html lang="en">
<head>
<meta charset="utf-8">
<title>Motorvane Ledger — Business Card</title>
<link href="https://fonts.googleapis.com/css2?family=Lobster+Two:ital,wght@1,700&family=Open+Sans:wght@400;800&display=swap" rel="stylesheet">
<style>
  :root {
    --backdrop: #ecebe8;
    --paper: #f7f7f7;
    --paper-shade: #e4e4e4;
    --grey-dark: #8a8a8a;
    --grey-mid: #a9a9a9;
    --grey-light: #c9c9c9;
    --ink: #4a4a4a;
    --ink-soft: #6b6b6b;
    --logo-dark: #1e1e1e;
    --logo-faint: #a4a4a4;
  }
  * { box-sizing: border-box; margin: 0; padding: 0; }
  html, body { width: 1200px; height: 1023px; overflow: hidden; }
  body {
    background: var(--backdrop);
    font-family: "Open Sans", Arial, sans-serif;
    position: relative;
  }
  .card {
    position: absolute;
    left: 320px;
    width: 560px;
    height: 320px;
    overflow: hidden;
    background: var(--paper);
    box-shadow: 0 6px 18px rgba(0,0,0,.18);
  }
  .card--front { top: 150px; }
  .card--back { top: 550px; }

  /* Front */
  .front__contact {
    position: absolute; left: 0; top: 0; width: 300px; height: 100%;
    background: linear-gradient(160deg, #ffffff 0%, var(--paper) 55%, var(--paper-shade) 100%);
  }
  .front__divider {
    position: absolute; left: 300px; top: 0; width: 3px; height: 100%;
    background: var(--grey-light);
  }
  .person { position: absolute; left: 36px; top: 62px; }
  .person__name {
    font-family: "Lobster Two", cursive;
    font-style: italic; font-weight: 700;
    font-size: 25px; color: var(--ink);
  }
  .person__role {
    font-size: 10px; color: var(--ink-soft); margin-left: 8px; margin-top: 2px;
  }
  .phones {
    position: absolute; left: 36px; bottom: 52px;
    font-size: 14px; color: var(--ink-soft); line-height: 30px;
  }
  .front__brand-panel {
    position: absolute; left: 303px; top: 0; right: 0; height: 100%;
    background: linear-gradient(180deg, var(--grey-mid) 0%, #b9b9b9 100%);
  }
  .front__brand-band {
    position: absolute; left: 303px; right: 0; top: 110px; height: 100px;
    background: #ffffff;
    display: flex; align-items: center; justify-content: center; gap: 10px;
  }
  .brand-dot {
    width: 18px; height: 18px; border-radius: 50%; background: var(--logo-dark);
    flex: none;
  }
  .brand-name {
    font-weight: 800; text-transform: uppercase; line-height: .95;
    color: var(--logo-dark); font-size: 24px; letter-spacing: -.5px;
  }

  /* Back */
  .back__stripe-wide {
    position: absolute; left: 0; right: 0; bottom: 0; height: 58px;
    background: linear-gradient(90deg, var(--grey-dark), var(--grey-mid));
  }
  .back__stripe-line {
    position: absolute; left: 0; right: 0; height: 5px; background: var(--grey-light);
  }
  .back__stripe-line--one { bottom: 66px; }
  .back__stripe-line--two { bottom: 78px; height: 3px; background: var(--grey-mid); }
  .back__brand {
    position: absolute; left: 0; right: 0; top: 60px; height: 130px;
    display: flex; align-items: center; justify-content: center; gap: 18px;
  }
  .back__brand .brand-dot { width: 34px; height: 34px; background: var(--logo-faint); }
  .back__brand .brand-name { color: var(--logo-faint); font-size: 50px; letter-spacing: -1px; }
</style>
</head>
<body>
  <section class="card card--front" aria-label="Business card front">
    <div class="front__contact">
      <div class="person">
        <div class="person__name">Martin Sowerby</div>
        <div class="person__role">(President of operations)</div>
      </div>
      <div class="phones">
        <div>Phone: 888-247-6031</div>
        <div>Cell: 561-384-2706</div>
      </div>
    </div>
    <div class="front__divider"></div>
    <div class="front__brand-panel"></div>
    <div class="front__brand-band">
      <span class="brand-dot"></span>
      <span class="brand-name">Motorvane<br>Ledger</span>
    </div>
  </section>

  <section class="card card--back" aria-label="Business card back">
    <div class="back__brand">
      <span class="brand-dot"></span>
      <span class="brand-name">Motorvane<br>Ledger</span>
    </div>
    <div class="back__stripe-line back__stripe-line--two"></div>
    <div class="back__stripe-line back__stripe-line--one"></div>
    <div class="back__stripe-wide"></div>
  </section>
</body>
</html>
```